Redesign two existing website pages and one new landing page for dental office

I need to redesign two webpages on my dental website, the Home page (http://brelvoortdental.com) and the Dental Implant Services page (http://www.brelvoortdental.com/dental-implant-services) and also create a landing page for the Dental Implant Services page.

Please use the same color scheme, slogans and subtitles for the redesign pages and create a reserved video spot on each page. The video spots should not be too big but not too small either and positioned in a central key location on each of the pages. The final redesigned pages should communicate leadership, confidence and trust.

The new landing page for the Dental implant Services page must not have any hyperlinks on the page and must entice the viewer to give name and email before downloading a "Free" eBook called "Is a Fresh Smile Worth Waiting For?" Any added photo images to this new page must be smiling.
Updates

Project Deadline Extended Reason: I got feedback that my project was not long enough so I'm extending it by 5 days. Added Thursday, April 16, 2015

Target Market(s)

People who are middle-age to seniors.

Industry/Entity Type

Dental

Coding

Coded - Design and coding required

Number of Pages Required

3 page

Requirements
Must have
• Compatible with existing website colors and theme.

```html
<!DOCTYPE html>
<html lang="en">
<head>
<meta charset="utf-8">
<title>Brelvoort Dental Care – Home</title>
<link rel="stylesheet" href="https://fonts.googleapis.com/css2?family=Montserrat:wght@400;500;600&family=Arimo:wght@400;700&display=swap">
<style>
:root{
  --green-dark:#3c5f55;
  --green-mid:#3d6b5e;
  --green-light:#8ab5a5;
  --nav:#3a3a3a;
  --ink:#444;
  --muted:#666;
  --white:#fff;
  --hero-a:#f4f4f4;
  --hero-b:#d9d9d9;
}
*{box-sizing:border-box;margin:0;padding:0}
html,body{width:798px;height:1200px;overflow:hidden;background:var(--white)}
body{position:relative;font-family:"Arimo",Arial,sans-serif;color:var(--ink)}
.abs{position:absolute}
.heading{font-family:"Montserrat",Arial,sans-serif;font-weight:600}

/* header */
.brand{left:72px;top:24px;font-family:"Montserrat",sans-serif;font-weight:500;font-size:22px;color:var(--green-mid);display:flex;align-items:center;gap:8px}
.brand-dot{width:12px;height:12px;border-radius:50%;background:var(--green-light)}
.quick-link{top:22px;display:flex;gap:7px;align-items:center;font-size:9.5px;line-height:14px;color:#333}
.nav{left:0;top:78px;width:798px;height:30px;background:var(--nav)}
.nav a{position:absolute;top:9px;font-size:10.5px;color:var(--white);text-decoration:none;font-family:"Arimo",sans-serif}

/* hero */
.hero{left:0;top:108px;width:798px;height:245px;background:radial-gradient(ellipse at 40% 40%,var(--hero-a),var(--hero-b));}
.hero-photo{left:360px;top:108px;width:372px;height:240px;background:linear-gradient(160deg,#e8ddd2,#c9a98c 55%,#f1ece6);border-radius:0 0 0 40px}
.hero-title{left:68px;top:142px;font-size:23.5px;line-height:28px;color:var(--green-mid)}
.hero-text{left:68px;top:205px;width:340px;font-size:12.5px;line-height:20px;color:#555}
.btn-hero{left:68px;top:264px;width:112px;height:34px;border-radius:6px;background:var(--green-mid);color:var(--white);font-family:"Montserrat",sans-serif;font-size:12.5px;display:flex;align-items:center;justify-content:center;box-shadow:0 2px 4px rgba(0,0,0,.3)}

/* service panels */
.panel{top:347px;height:241px;color:var(--white);padding:8px 13px}
.panel-light{left:70px;width:330px;background:var(--green-light)}
.panel-dark{left:400px;width:331px;background:var(--green-dark);padding-left:37px}
.panel h2{font-size:16.5px;font-weight:600;font-family:"Montserrat",sans-serif}
.panel h3{font-size:12.5px;font-weight:400;font-family:"Montserrat",sans-serif;margin-top:2px}
.panel-img{width:272px;height:108px;margin-top:7px}
.panel p{font-size:8.8px;line-height:14.5px;margin-top:7px}
.panel .btn{display:inline-block;margin-top:8px;padding:7px 7px;font-family:"Montserrat",sans-serif;font-size:10px}
.panel-light .btn{background:var(--green-dark)}
.panel-dark .btn{background:var(--green-light)}

/* features */
.feature{top:630px;width:170px}
.feature-icon{width:56px;height:56px;border-radius:50%;background:var(--green-mid);display:flex;align-items:center;justify-content:center}
.feature h4{font-family:"Montserrat",sans-serif;font-weight:600;font-size:12.5px;color:#444;margin-top:22px}
.bullets{list-style:none;margin-top:10px}
.bullets li{font-size:8.8px;line-height:16px;color:#444;padding-left:10px;position:relative}
.bullets li::before{content:"";position:absolute;left:0;top:6px;width:4px;height:4px;border-radius:50%;background:#444}

/* cta band */
.cta{left:67px;top:814px;width:664px;height:71px;border-radius:8px;background:var(--green-light)}
.cta-text{left:80px;top:839px;font-size:15.5px;color:var(--white)}
.cta-btn{left:618px;top:828px;width:98px;height:44px;border-radius:6px;background:var(--green-mid);color:var(--white);font-family:"Montserrat",sans-serif;font-size:11px;text-align:center;line-height:14px;padding-top:8px}

/* lower columns */
.col-title{top:908px;font-size:16px;color:var(--green-mid)}
.col-img{left:82px;top:938px;width:193px;height:84px;background:linear-gradient(120deg,#e9eef2,#b8c7d2 60%,#f2f4f6)}
.col-text{left:80px;top:1028px;width:192px;font-size:7.6px;line-height:12px;color:#555;text-align:justify}
.blog-list{left:316px;top:934px}
.blog-list li{line-height:18.6px}
.video{left:552px;top:939px;width:179px;height:112px;background:#2a2a2a;border:1px solid #ccc}
.video-inner{position:absolute;left:4px;top:12px;right:4px;bottom:14px;background:linear-gradient(120deg,#5a3a2a,#8a6a52)}
.video-cap{position:absolute;left:4px;top:2px;font-size:5px;color:#ddd}
.video-bar{position:absolute;left:4px;right:4px;bottom:4px;height:5px;background:#555}
.play{position:absolute;left:80px;top:40px;width:20px;height:14px;border-radius:3px;background:#1a1a1a}
.about-link{left:668px;top:1062px;font-size:9px;color:var(--green-mid);text-decoration:underline}

/* footer */
.footer{left:0;top:1084px;width:798px;height:116px;background:var(--green-dark);color:var(--white)}
.social{position:absolute;top:10px;width:21px;height:21px;background:#ccc;border-radius:2px}
.foot-links{position:absolute;left:72px;top:48px;font-size:9.5px}
.foot-copy{position:absolute;left:72px;top:68px;font-size:9.3px;line-height:15px}
.foot-phone{position:absolute;left:544px;top:20px;font-family:"Montserrat",sans-serif;font-size:19px;display:flex;align-items:center;gap:10px}
.foot-brand{position:absolute;left:544px;top:64px;font-family:"Montserrat",sans-serif;font-weight:500;font-size:19px;color:#cfdcd7}
</style>
</head>
<body>

<header>
  <div class="abs brand"><span class="brand-dot"></span>Brelvoort Dental Care</div>
  <div class="abs quick-link" style="left:400px">
    <svg width="26" height="30" viewBox="0 0 26 30"><rect x="2" y="2" width="13" height="24" rx="2" fill="none" stroke="#555" stroke-width="1.6"/><rect x="12" y="10" width="11" height="18" rx="2" fill="#fff" stroke="#555" stroke-width="1.6"/></svg>
    <span>Get Dr. Brelvoort's<br>Mobile App</span>
  </div>
  <div class="abs quick-link" style="left:518px">
    <svg width="30" height="30" viewBox="0 0 30 30"><rect x="2" y="2" width="18" height="22" fill="none" stroke="#555" stroke-width="1.6"/><circle cx="20" cy="20" r="8" fill="#fff" stroke="#555" stroke-width="1.6"/><path d="M20 15v5h4" fill="none" stroke="#555" stroke-width="1.6"/></svg>
    <span>Request an<br>Appointment</span>
  </div>
  <div class="abs quick-link" style="left:632px">
    <svg width="28" height="30" viewBox="0 0 28 30"><path d="M4 3h14l6 6v19H4z" fill="none" stroke="#555" stroke-width="1.6"/><path d="M8 12h12M8 16h12M8 20h12" stroke="#555" stroke-width="1.4"/></svg>
    <span>New Patient<br>Online Forms</span>
  </div>
</header>

<nav class="abs nav">
  <a style="left:83px">HOME</a>
  <a style="left:167px">ABOUT US</a>
  <a style="left:273px">DENTAL SERVICES</a>
  <a style="left:418px">BLOG</a>
  <a style="left:499px">CONTACT US</a>
  <a style="left:617px">TESTIMONIALS</a>
</nav>

<section>
  <div class="abs hero"></div>
  <div class="abs hero-photo" role="img" aria-label="Photo of a smiling family of four"></div>
  <h1 class="abs heading hero-title">Life-Changing Family Dental<br>Care In Sugar Land</h1>
  <p class="abs hero-text">In this section you may find how our doctor treat with our patient and other lorem ipsum thing.</p>
  <div class="abs btn-hero">Appointment</div>
</section>

<section>
  <div class="abs panel panel-light">
    <h2>Dental Hygiene Services</h2>
    <h3>Achieve Better Health With Prevention</h3>
    <div class="panel-img" role="img" aria-label="Photo of a smiling woman brushing her teeth" style="background:linear-gradient(120deg,#f3f3f3,#d8c3b2 60%,#f5f5f5)"></div>
    <p>Maintain healthy teeth and gums with consistent dental exams and teeth cleanings by one of our professional dental hygienists.</p>
    <span class="btn">Learn More</span>
  </div>
  <div class="abs panel panel-dark">
    <h2>Dental Emergency Services</h2>
    <h3>Stop Pain From Tooth Trauma and Infection</h3>
    <div class="panel-img" role="img" aria-label="Photo of a dentist examining a patient's teeth" style="background:linear-gradient(120deg,#cfdbe6,#e9eef2 50%,#d9b7a3)"></div>
    <p>Maintain healthy teeth and gums with consistent dental exams and teeth cleanings by one of our professional dental hygienists.</p>
    <span class="btn">Learn More</span>
  </div>
  <svg class="abs" style="left:373px;top:455px" width="52" height="52" viewBox="0 0 52 52">
    <circle cx="26" cy="26" r="25" fill="#ddd"/><circle cx="26" cy="26" r="22" fill="#222"/>
    <path d="M18 18c3-3 6-1 8 0 2-1 5-3 8 0 3 4 0 9-1 12-1 4-2 9-4 9s-2-6-3-6-1 6-3 6-3-5-4-9c-1-3-4-8-1-12z" fill="none" stroke="#fff" stroke-width="2"/>
  </svg>
</section>

<section>
  <div class="abs feature" style="left:70px">
    <div class="feature-icon" style="margin-left:34px"><svg width="24" height="22" viewBox="0 0 24 22"><rect x="1" y="5" width="22" height="16" rx="2" fill="#fff"/><rect x="8" y="1" width="8" height="5" fill="none" stroke="#fff" stroke-width="2"/><path d="M12 9v9M7.5 13.5h9" stroke="#3d6b5e" stroke-width="3"/></svg></div>
    <h4>Beautiful Dentures</h4>
    <ul class="bullets"><li>What is a Denture?</li><li>Who Needs a Denture?</li><li>Just How Are Dentures Made?</li></ul>
  </div>
  <div class="abs feature" style="left:245px">
    <div class="feature-icon" style="margin-left:33px"><svg width="26" height="20" viewBox="0 0 26 20"><path d="M1 6h6l3-5h15v15H1z" fill="#fff"/><circle cx="6" cy="17" r="2.5" fill="#fff" stroke="#3d6b5e"/><circle cx="20" cy="17" r="2.5" fill="#fff" stroke="#3d6b5e"/><path d="M17 4v7M13.5 7.5h7" stroke="#3d6b5e" stroke-width="2.4"/></svg></div>
    <h4>Cosmetic Dentistry</h4>
    <ul class="bullets"><li>What is a Denture?</li><li>Who Needs a Denture?</li><li>Just How Are Dentures Made?</li></ul>
  </div>
  <div class="abs feature" style="left:411px">
    <div class="feature-icon" style="margin-left:39px"><svg width="20" height="22" viewBox="0 0 20 22"><circle cx="10" cy="6" r="5" fill="#fff"/><path d="M1 21c0-6 4-9 9-9s9 3 9 9z" fill="#fff"/><circle cx="10" cy="17" r="2" fill="#3d6b5e"/></svg></div>
    <h4>Dental Implant Services</h4>
    <ul class="bullets"><li>What is a Denture?</li><li>Who Needs a Denture?</li><li>Just How Are Dentures Made?</li></ul>
  </div>
  <div class="abs feature" style="left:607px">
    <div class="feature-icon" style="margin-left:26px"><svg width="20" height="24" viewBox="0 0 20 24"><path d="M3 2v7a5 5 0 0 0 10 0V2" fill="none" stroke="#fff" stroke-width="2.4"/><path d="M8 14v3a4 4 0 0 0 8 0v-4" fill="none" stroke="#fff" stroke-width="2.4"/><circle cx="16" cy="11" r="2.4" fill="#fff"/></svg></div>
    <h4>Sedation Dentistry</h4>
    <ul class="bullets" style="margin-top:12px"><li>Control Dental Fear</li><li>Dental Pain Management</li><li>Relaxed and Tranquil</li></ul>
  </div>
</section>

<section>
  <div class="abs cta"></div>
  <div class="abs heading cta-text">Comprehensive Family Dentistry in One Sugar Land Dental Office!</div>
  <div class="abs cta-btn">An<br>Appointment?</div>
</section>

<section>
  <h2 class="abs heading col-title" style="left:82px">Don't Wait 'til it Hurts!</h2>
  <div class="abs col-img" role="img" aria-label="Photo of a dentist and assistant treating a patient"></div>
  <p class="abs col-text">Get acquanted today with comfortable dental care.Request an Appointment! We will contact you right away to schedule your dental appointment.</p>

  <h2 class="abs heading col-title" style="left:316px;top:906px">Recent Blog Posts</h2>
  <ul class="abs bullets blog-list">
    <li>Conscious Sedation: A Way to Deal with</li>
    <li>Anxiety at the Dentist's Office</li>
    <li>Pediatric Dentists and Their Importance in</li>
    <li>Today's World</li>
    <li>Tooth Implant Facts</li>
    <li>Is Sedation Dentistry Cost Affordable?</li>
    <li>How to Prepare for Oral Surgery</li>
  </ul>

  <h2 class="abs heading col-title" style="left:552px">Dr. Paul Brelvoort</h2>
  <div class="abs video">
    <span class="video-cap">Meet Your Sugar Land Family Dentist Today</span>
    <div class="video-inner" role="img" aria-label="Video still of the dentist speaking in his office"></div>
    <div class="play"><svg width="20" height="14"><path d="M8 4l5 3-5 3z" fill="#fff"/></svg></div>
    <div class="video-bar"></div>
  </div>
  <div class="abs about-link">● About Doctor</div>
</section>

<footer class="abs footer">
  <span class="social" style="left:74px"></span>
  <span class="social" style="left:99px"></span>
  <span class="social" style="left:124px"></span>
  <span class="social" style="left:149px"></span>
  <span class="social" style="left:174px"></span>
  <div class="foot-links">Home &nbsp;|&nbsp; About Us &nbsp;|&nbsp; Dental Services &nbsp;|&nbsp; Blog &nbsp;|&nbsp; Contact Us &nbsp;|&nbsp; Testimonials</div>
  <div class="foot-copy">©2014 Brelvoort Dental Care, Westpark Medical Plaza, 2400 Orchard Lane, Ste.<br>#120, Sugar Land, TX 77479</div>
  <div class="foot-phone">
    <svg width="20" height="20" viewBox="0 0 20 20"><circle cx="10" cy="10" r="9" fill="none" stroke="#fff" stroke-width="1.4"/><path d="M7 5l2 3-1 1c1 2 2 3 3 3l1-1 3 2-1 2c-4 0-8-4-8-8z" fill="#fff"/></svg>
    (281) 555-0147
  </div>
  <div class="foot-brand">Brelvoort Dental Care</div>
</footer>

</body>
</html>
```